Brochure Design Project

We need a brochure design for our apparent company - Harborline Freight.(Tri-fold - 8 1/2 x 14)

About-
Harborline Freight is Southern California's Class A 3PL, providing excellence in storage and materials handling for all industrial and consumer products.

Description-
Harborline Depot Inc. is a family owned warehousing and distribution business based in Southern California. Poised to serve domestic US and international companies, Harborline is able to provide Class A terminals in La Mirada and Mira Loma. Total warehouse available approximates 200,000 sf, managed with state of the art third party logistics software to ensure accuracy and transparency for each client.

Every account is handled with a dedicated customer service representative who is able to process both industrial bulk shipments right through to drop ship enquiries. Picking and packing individual items is perfect for E-Commerce businesses which require

Harborline also strives to support the industry in environmental stewardship, incorporating a variety of energy-efficient practices and utilizing low-emission vehicles to minimize its carbon footprint. In addition, a recycling program has been implemented for all waste material.

Recent customer feedback revealed that a significant reason customers are referred to Harborline or have been long standing customers with Harborline is due to the trust and reliability the team demonstrates each and every day. With real time tracking inbound and outbound inventory control, we pride ourselves in expediting shipments from large right through to small pick and pack orders. Harborline understands that every business is different, from the different types of products and clientele, from business-to-business to business-to-consumer.

Website:
www.harborlinefreight-demo.com - Use this as a idea of what we are looking for and be sure to add the Services of what we do to the brochure
Address:
27356 Pellham Ave.
Crestmoor, CA 90651
Ph:
310-555-0172
Put all social media outlets: Facebook, Twitter, LinkedIN, Google+

**require .psd file**

This project has an updated time table to be finished by April 15, 2013.

Target Market(s)

Company looking for warehousing and logistics.

Industry/Entity Type

Industrial

Requirements
Must have
• Website:
Address:
27356 Pellham Ave.
Crestmoor, CA 90651
Ph:
310-555-0172

QR on the back linking to the website

```html
<!DOCTYPE html>
<html lang="en">
<head>
<meta charset="utf-8">
<title>Harborline Freight – Brochure Concept 2</title>
<link href="https://fonts.googleapis.com/css2?family=Ubuntu:wght@400;500;700&family=Fira+Sans:ital,wght@1,400;1,600&family=Maven+Pro:wght@400;700&display=swap" rel="stylesheet">
<style>
:root{
  --stage:#efedea;
  --white:#ffffff;
  --paper:#f4f5f6;
  --brand:#1a6fb8;
  --cyan:#19a6d9;
  --navy:#132a40;
  --ink:#3a3a3a;
  --quote:#555a60;
  --muted:#9fb3c2;
  --label:#7d7a76;
  --footer-ink:#b9a892;
}
*{margin:0;padding:0;box-sizing:border-box}
html,body{width:1200px;height:900px;overflow:hidden}
body{background:var(--stage);font-family:"Ubuntu",sans-serif;position:relative}
.panel{position:absolute;top:158px;height:478px;overflow:hidden;box-shadow:0 1px 4px rgba(0,0,0,.18)}
.panel-label{position:absolute;top:674px;font-size:17px;color:var(--label)}

/* cover */
.cover{left:33px;width:258px;background:var(--paper)}
.cover .map-art{position:absolute;inset:0 0 39px 0;background:linear-gradient(160deg,#f7f8f9,#e9ecee 60%,#f2f3f4)}
.brand-lockup{position:absolute;display:flex;align-items:center;gap:6px}
.brand-lockup .dot{width:22px;height:22px;border-radius:50%;background:var(--brand)}
.brand-lockup .name{font-weight:700;color:var(--brand);font-size:25px}
.cover .brand-lockup{left:22px;top:124px}
.cover .web{position:absolute;left:22px;top:393px;font-size:10px;color:var(--muted)}
.cover .foot-band{position:absolute;left:0;right:0;bottom:0;height:39px;background:#d6d7d8}

/* back */
.back{left:318px;width:264px;background:var(--white)}
.back .edge{position:absolute;left:0;top:0;bottom:0;width:23px;background:linear-gradient(var(--brand),var(--cyan) 60%,var(--brand))}
.quote{position:absolute;left:55px;width:126px;font-family:"Fira Sans",sans-serif;font-style:italic;font-size:10px;line-height:1.15;color:var(--quote)}
.quote cite{display:block;margin-top:10px;font-weight:600;font-size:10.5px;color:var(--cyan);font-style:italic}
.quote cite span{display:block;font-weight:400;font-size:10px}
.quote.one{top:34px}
.quote.two{top:187px}
.contact{position:absolute;left:23px;right:0;bottom:0;height:144px;background:var(--navy);padding:12px 0 0 23px;color:#e6eef5}
.contact h2{font-weight:400;font-size:18px;color:#5fc3ea;margin-bottom:12px}
.contact ul{list-style:none;font-size:10px}
.contact li{display:flex;gap:10px;margin-bottom:11px;align-items:flex-start}
.contact svg{width:13px;height:13px;flex:none}
.social{position:absolute;right:34px;top:14px;display:flex;flex-direction:column;gap:8px}
.social span{width:21px;height:21px;border-radius:50%;background:var(--cyan)}
.social span.alt{background:#d9432f}

/* p2 */
.p2{left:620px;width:258px;background:var(--white)}
.p2 .dots{position:absolute;left:22px;top:28px;display:flex;flex-direction:column;gap:10px}
.p2 .dots span{width:18px;height:18px;border-radius:50%}
.p2 .vertical-brand{position:absolute;left:20px;bottom:16px;transform:rotate(-90deg);transform-origin:left bottom;translate:25px 0;display:flex;align-items:center;gap:5px}
.p2 .vertical-brand .name{font-weight:700;color:var(--brand);font-size:22px}
.p2 .vertical-brand .dot{width:16px;height:16px;border-radius:50%;background:var(--brand)}
.p2 .photo{position:absolute;left:64px;top:0;right:0;bottom:0;background:radial-gradient(circle at 45% 75%,#3b8fe0,#1a5ea8 30%,transparent 45%),linear-gradient(160deg,#6dc6f0,#1f6fb5 45%,#0c3568)}

/* p3 */
.p3{left:878px;width:267px;background:var(--white);padding:22px 20px 0 40px}
.p3 h1{font-family:"Maven Pro",sans-serif;font-weight:400;font-size:21px;color:var(--cyan);margin-bottom:10px}
.p3 p{font-size:7.6px;line-height:1.55;color:var(--ink);text-align:justify;margin-bottom:9px}
.p3 .sign{text-align:right;font-size:7.6px;color:var(--ink);font-style:italic;margin-top:20px}
.p3 .sign strong{display:block;font-style:normal;color:var(--cyan);margin-top:8px}
.p3 .web{position:absolute;left:40px;bottom:38px;font-size:8px;color:var(--muted)}

.footer{position:absolute;left:0;right:0;top:800px;bottom:0;background:var(--white)}
.footer h3{position:absolute;left:33px;top:38px;font-family:"Maven Pro",sans-serif;font-weight:400;font-size:25px;letter-spacing:1.5px;color:var(--footer-ink)}
.footer h3 b{font-weight:700}
</style>
</head>
<body>

<section class="panel cover">
  <div class="map-art" role="img" aria-label="Faint world map line drawing"></div>
  <div class="brand-lockup"><span class="dot"></span><span class="name">Harborline</span></div>
  <p class="web">harborlinefreight-demo.com</p>
  <div class="foot-band"></div>
</section>
<span class="panel-label" style="left:33px">cover</span>

<section class="panel back">
  <div class="edge"></div>
  <blockquote class="quote one">"Northgate Polymers has been utilizing the Harborline warehouse for approximately 10 years. We are able to ship full truckloads weekly to accommodate our West Coast customers. We are based in"
    <cite>Northgate Polymers<span>Linden Falls, Ohio</span></cite></blockquote>
  <blockquote class="quote two">"The services received from Harborline Freight are superior!. Their employees are very courteous and always willing to assist our needs in every way possible. Our inventory can be accessed via
    <cite>Redmill Textiles<span>Cedar Ridge, Georgia "</span></cite></blockquote>
  <div class="contact">
    <h2>Harborline Freight</h2>
    <ul>
      <li><svg viewBox="0 0 16 16"><path d="M3 2h3l1 4-2 1a8 8 0 0 0 4 4l1-2 4 1v3a1 1 0 0 1-1 1A12 12 0 0 1 2 3a1 1 0 0 1 1-1z" fill="#cfe3f2"/></svg>310-555-0172</li>
      <li><svg viewBox="0 0 16 16"><path d="M8 2 1 8h2v6h4v-4h2v4h4V8h2z" fill="#cfe3f2"/></svg>info@harborline-demo.com</li>
      <li><svg viewBox="0 0 16 16"><path d="M1 3h14v10H1z" fill="#cfe3f2"/><path d="M1 3l7 6 7-6" stroke="#132a40" fill="none"/></svg>27356 Pellham Ave.<br>Crestmoor, CA 90651.</li>
    </ul>
    <div class="social"><span></span><span></span><span class="alt"></span><span></span></div>
  </div>
</section>
<span class="panel-label" style="left:318px">back</span>

<section class="panel p2">
  <div class="dots"><span style="background:var(--brand)"></span><span style="background:var(--cyan)"></span><span style="background:#8fb4c4"></span></div>
  <div class="vertical-brand"><span class="dot"></span><span class="name">Harborline</span></div>
  <div class="photo" role="img" aria-label="Blue-toned warehouse interior with forklift and a globe"></div>
</section>
<span class="panel-label" style="left:620px">p2</span>

<section class="panel p3">
  <h1>Presidents Message</h1>
  <p>Firstly thank you for taking the time to review our website. The business has come a long way and I have only to thank our very loyal customers and staff who have stuck with us for a long time. As everyone knows the logistics business is fairly competitive and often the challenge is meeting the needs of every single customer for the right value. The investment I make personally, is in the everyday operational issues to make sure each customer, receives value for their investment with us. Each and every transaction is monitored and every person is held accountable. With Meridian, our Warehouse Management Software we provide full visibility to our customers. Tracking your inventoried items is made easy with a secured gateway to our systems giving our customers the ability to export inventory and transactional reports as required. Our customers are based both globally and in various parts of the USA. Our locations in Southern California offer great advantages as we are strategically positioned not too far from the Port of Long Beach and geographically located in between Los Angeles County and Orange County.</p>
  <p>My vision for the business is not only growth. But growth without compromising the quality of service we provide today. Each customer service representative has a good handle on an individual customer and we will continue to provide a very personal service.</p>
  <div class="sign">Respectfully,<strong>Paul Navarro.</strong></div>
  <p class="web">harborlinefreight-demo.com</p>
</section>
<span class="panel-label" style="left:892px">p3 / p5</span>

<footer class="footer"><h3>BROCHURE DESIGN - <b>CONCEPT 2</b></h3></footer>
</body>
</html>
```